Sunwellflow Aquadeepflow Depot

Need a brochure to send to new prospective clients, giving them an idea of what we are and what we can do for them.
To be sent as an attachment to an email.
Printable if possible to hand out at Pastoral Expo Week.
http://www.sunwellflow.com.au/
http://www.aquadeepflow.com.au/
http://www.wellflowy.net.au/
All three of these site are part of what I do.

Target Market(s)

Rural, Sheep and cattle stations, water bore users, out of city living.

Colors
0255a3
0692cd

Requirements
Must have
• Print and email version

```html
<!DOCTYPE html>
<html lang="en">
<head>
<meta charset="utf-8">
<title>Sunwellflow – How To Guides</title>
<link rel="stylesheet" href="https://fonts.googleapis.com/css2?family=Roboto:wght@300;400;500;700&family=Montserrat:wght@700&display=swap">
<style>
  :root {
    --brand-blue: #0255a3;
    --sky-blue: #0692cd;
    --bright-blue: #12a6ee;
    --orange: #f39a0b;
    --ink: #1d1d1f;
    --paper: #f4f5f6;
  }
  * { margin: 0; padding: 0; box-sizing: border-box; }
  html, body { width: 848px; height: 1200px; overflow: hidden; background: #fff; }
  .sheet {
    position: relative; width: 848px; height: 1200px; overflow: hidden;
    background: linear-gradient(180deg, #fff 0%, var(--paper) 40%, #eceeef 100%);
    font-family: "Roboto", Arial, sans-serif; color: var(--ink);
  }
  .abs { position: absolute; }
  .header-art, .footer-art { position: absolute; left: 0; }
  .header-art { top: 0; }
  .footer-art { top: 1080px; }
  .brand-title {
    position: absolute; left: 468px; top: 44px;
    font-size: 37px; font-weight: 300; color: #fff; letter-spacing: 0.5px;
  }
  .field-backdrop {
    position: absolute; left: 0; top: 700px; width: 848px; height: 396px;
    background: radial-gradient(ellipse at 55% 45%, rgba(150,155,160,0.35), rgba(220,222,224,0.15) 60%, rgba(255,255,255,0) 80%);
  }
  .photo {
    position: absolute; border-radius: 50%;
    border: 5px solid var(--sky-blue);
    box-shadow: -4px -3px 0 var(--orange);
  }
  .photo-hero { left: 30px; top: 202px; width: 176px; height: 176px;
    background: linear-gradient(135deg, #8a9aa6, #c7b89a 55%, #6d7a56); }
  .photo-step { left: 22px; width: 114px; height: 114px;
    background: radial-gradient(circle at 50% 45%, #5a5f63, #2a2d30 70%); }
  .guides-title {
    left: 256px; top: 188px; font-size: 25px; font-weight: 700; color: var(--brand-blue);
  }
  .guide-list { list-style: none; }
  .guide-list li {
    position: absolute; font-size: 16.2px; display: flex; align-items: center; gap: 14px; white-space: nowrap;
  }
  .guide-list svg { width: 22px; height: 18px; flex: none; }
  .intro {
    left: 20px; width: 808px; font-size: 15.6px; line-height: 20.4px; text-align: justify;
  }
  .section-title {
    left: 158px; top: 572px; font-size: 24.5px; font-weight: 700; color: var(--brand-blue);
  }
  .body-copy {
    left: 158px; width: 668px; font-size: 15.6px; line-height: 20.4px; text-align: justify;
  }
  .phone {
    left: 44px; top: 1116px; display: flex; align-items: center; gap: 16px;
    font-family: "Montserrat", Arial, sans-serif; font-weight: 700; font-size: 49px; color: #fff; letter-spacing: -0.5px;
  }
  .phone svg { width: 42px; height: 42px; }
  .web {
    left: 586px; top: 1158px; font-size: 16px; color: var(--ink);
  }
</style>
</head>
<body>
<div class="sheet">

  <svg class="header-art" width="848" height="180" viewBox="0 0 848 180" aria-hidden="true">
    <defs>
      <linearGradient id="bandBlue" x1="0" x2="1">
        <stop offset="0" stop-color="#0a8fd8"/>
        <stop offset="1" stop-color="#0255a3"/>
      </linearGradient>
    </defs>
    <polygon points="0,14 312,14 232,98 0,98" fill="url(#bandBlue)"/>
    <polygon points="300,0 848,0 848,20 282,20" fill="#0255a3"/>
    <polygon points="470,20 848,20 848,112 380,112" fill="#12a6ee"/>
    <polygon points="395,112 848,112 848,136 168,136 236,112" fill="#f39a0b"/>
    <polygon points="330,0 342,0 142,174 130,174" fill="#0255a3"/>
    <polygon points="348,18 358,18 170,166 160,166" fill="#f39a0b"/>
  </svg>
  <div class="brand-title">SUNWELLFLOW</div>

  <div class="photo photo-hero" role="img" aria-label="Technician in hi-vis shirt adjusting a solar pump controller"></div>

  <h2 class="abs guides-title">HOW TO GUIDES</h2>
  <ul class="guide-list">
    <li style="left:252px;top:236px"><svg viewBox="0 0 22 18"><rect x="2" y="5" width="18" height="10" fill="none" stroke="#0255a3" stroke-width="1.6"/><path d="M2 10H20M8 5V15M14 5V15M9 17H13" stroke="#0255a3" stroke-width="1.4"/><circle cx="11" cy="2" r="1.6" fill="#f39a0b"/></svg>Submersible Pump Selection</li>
    <li style="left:252px;top:267px"><svg viewBox="0 0 22 18"><rect x="2" y="5" width="18" height="10" fill="none" stroke="#0255a3" stroke-width="1.6"/><path d="M2 10H20M8 5V15M14 5V15M9 17H13" stroke="#0255a3" stroke-width="1.4"/><circle cx="11" cy="2" r="1.6" fill="#f39a0b"/></svg>Submersible Pump Shroud</li>
    <li style="left:252px;top:298px"><svg viewBox="0 0 22 18"><rect x="2" y="5" width="18" height="10" fill="none" stroke="#0255a3" stroke-width="1.6"/><path d="M2 10H20M8 5V15M14 5V15M9 17H13" stroke="#0255a3" stroke-width="1.4"/><circle cx="11" cy="2" r="1.6" fill="#f39a0b"/></svg>Submersible Cable Splice</li>
    <li style="left:252px;top:330px"><svg viewBox="0 0 22 18"><rect x="2" y="5" width="18" height="10" fill="none" stroke="#0255a3" stroke-width="1.6"/><path d="M2 10H20M8 5V15M14 5V15M9 17H13" stroke="#0255a3" stroke-width="1.4"/><circle cx="11" cy="2" r="1.6" fill="#f39a0b"/></svg>Submersible Pump Installation</li>
    <li style="left:570px;top:236px"><svg viewBox="0 0 22 18"><rect x="2" y="5" width="18" height="10" fill="none" stroke="#0255a3" stroke-width="1.6"/><path d="M2 10H20M8 5V15M14 5V15M9 17H13" stroke="#0255a3" stroke-width="1.4"/><circle cx="11" cy="2" r="1.6" fill="#f39a0b"/></svg>Solar Pump Installation</li>
    <li style="left:570px;top:267px"><svg viewBox="0 0 22 18"><rect x="2" y="5" width="18" height="10" fill="none" stroke="#0255a3" stroke-width="1.6"/><path d="M2 10H20M8 5V15M14 5V15M9 17H13" stroke="#0255a3" stroke-width="1.4"/><circle cx="11" cy="2" r="1.6" fill="#f39a0b"/></svg>Solar Panel Installation</li>
    <li style="left:570px;top:298px"><svg viewBox="0 0 22 18"><rect x="2" y="5" width="18" height="10" fill="none" stroke="#0255a3" stroke-width="1.6"/><path d="M2 10H20M8 5V15M14 5V15M9 17H13" stroke="#0255a3" stroke-width="1.4"/><circle cx="11" cy="2" r="1.6" fill="#f39a0b"/></svg>Pressure Switch Adjustment</li>
    <li style="left:570px;top:330px"><svg viewBox="0 0 22 18"><rect x="2" y="5" width="18" height="10" fill="none" stroke="#0255a3" stroke-width="1.6"/><path d="M2 10H20M8 5V15M14 5V15M9 17H13" stroke="#0255a3" stroke-width="1.4"/><circle cx="11" cy="2" r="1.6" fill="#f39a0b"/></svg>Fault Finding Guide</li>
    <li style="left:333px;top:373px"><svg viewBox="0 0 22 18"><rect x="2" y="5" width="18" height="10" fill="none" stroke="#0255a3" stroke-width="1.6"/><path d="M2 10H20M8 5V15M14 5V15M9 17H13" stroke="#0255a3" stroke-width="1.4"/><circle cx="11" cy="2" r="1.6" fill="#f39a0b"/></svg>Hydrovance SafeGuard AUTO set up</li>
  </ul>

  <p class="abs intro" style="top:410px">This guide contains information on how to choose the correct submersible pump, how to prepare the pump and components for installation, and how to adjust the controls and switches once the pump is installed. The fault finding guide is also included to assist with finding the problem and it’s possible cause.</p>
  <p class="abs intro" style="top:483px">I have put this guide together based on experience gained as a mechanical / elec-trical tradesman over the last 35 years working in residential back yards, industri-al sites and mine sites, Drilling Water bores, install-ing pumps and associated equipment and fault finding.</p>

  <div class="field-backdrop" role="img" aria-label="Faded solar panel array in a dry paddock"></div>

  <h2 class="abs section-title">Tecramatic XPS Pressure Switch Adjustment</h2>

  <div class="photo photo-step" style="top:630px" role="img" aria-label="Pressure switch mounted beneath the pressure tank"></div>
  <div class="photo photo-step" style="top:796px" role="img" aria-label="Pressure switch with cover and fittings"></div>
  <div class="photo photo-step" style="top:958px" role="img" aria-label="Pressure switch adjustment dial marked with an arrow"></div>

  <p class="abs body-copy" style="top:612px">The pressure switch is used to switch the pump drive motor off when the pump system is up to its required pressure, when all of the valves are closed and their is no further demand for water. The pressure tank stores a volume of water so the pump will not start if the system settles or leaks slightly. In this example the pressure switch is the black box under the pressure tank. Always disconnect the power supply from the pressure switch and test with a multimeter to ensure the switch is not live before removing the cover.</p>
  <p class="abs body-copy" style="top:771px">A correctly charged pressure tank and correctly set pressure switch will allow the pump to shut off when there is no demand for water and restart when the pressure drops due to a demand or requirement for more water. The pressure switch contacts should remain closed and the pump running while the demand for water is present. That means the pump will run constantly while filling the tank or watering the garden. If the pressure switch is out of adjustment the pump will stop and start and cycle between on and off while in use. This condition of cycling or rapid cycling will damage the pump and motor and consume a large amount of power.</p>
  <p class="abs body-copy" style="top:950px">Adjustment of the pressure switch is made while the power is isolated from the pump. To increase the cut out pressure of the Tecramatic XPS pressure switch turn the large thumb dial clockwise. Reconnect the power and allow the pump to run in its normal operating condition. If the pressure switch allows the pump to cycle on and off unneces-sarily. Isolate the power and increase the pressure further. Always check that the pump can reach the set cut out pressure and stop when the valves are closed.</p>

  <svg class="footer-art" width="848" height="120" viewBox="0 1080 848 120" aria-hidden="true">
    <rect x="0" y="1184" width="848" height="16" fill="#f2f3f4"/>
    <polygon points="480,1116 744,1116 820,1200 560,1200" fill="#12a6ee"/>
    <polygon points="520,1144 848,1144 848,1200 566,1200" fill="#f39a0b"/>
    <polygon points="0,1096 460,1096 552,1184 0,1184" fill="#0255a3"/>
  </svg>

  <div class="abs phone">
    <svg viewBox="0 0 42 42" aria-hidden="true">
      <path d="M10 6 L16 6 L19 14 L15 17 Q18 24 25 27 L28 23 L36 26 L36 32 Q34 37 28 36 Q12 32 6 14 Q6 8 10 6 Z" fill="#fff"/>
      <path d="M25 7 A10 10 0 0 1 35 17" stroke="#fff" stroke-width="2.6" fill="none" stroke-linecap="round"/>
      <path d="M24 13 A5 5 0 0 1 29 18" stroke="#fff" stroke-width="2.6" fill="none" stroke-linecap="round"/>
    </svg>
    1300 555 019
  </div>
  <div class="abs web">www.sunwellflow.com.au</div>
</div>
</body>
</html>
```